Vessa Kliniq - Dermatology Consultation App

Vessa Kliniq is launching a new Pindle IOS App for online Dermatology consultation. We would appreciate a simple Scandinavian design which communicates trust, comfort and expensive feel. Most yacht designs have similar color palette, light wood colors and textures, but don’t be restricted by those in your artistic search.
The process is completed in three easy steps:
1. take a Snapshot.
2. Describe and Send it.
3. get Diagnosis and Treatment.
The Home screen should also have buttons - Start new Case, Follow up Visit, Rx Refill.
15% of the Home screen should also have a field/button - Medical Cosmetics Shop.
10% of the Home screen should also have a field or buttons for Our Partners (sponsors) – Lumavel, Norvexa, Toral, Ostra. (if you click you would be directed to their sites)
Note / Suggestion : Maybe you could use a larger picture of a dermatologist and have overlying fields and content, just for more influencing effect. (I am not a professional though)
Thank you so much.
24 - 59 Female
Club

```html
<!DOCTYPE html>
<html lang="en">
<head>
<meta charset="utf-8">
<title>Vessa Kliniq – Dermatology Consultation</title>
<link rel="stylesheet" href="https://fonts.googleapis.com/css2?family=Alegreya:wght@500&family=Roboto+Condensed:wght@300;400&display=swap">
<style>
  :root {
    --canvas: #ebe5dc;
    --plum-deep: #5f4a5e;
    --plum: #6f5a6e;
    --plum-light: #8d7587;
    --gold: #cda862;
    --copper: #c1915f;
    --aubergine: #4b3846;
    --ivory: #f4eef1;
    --mist: rgba(244, 238, 241, 0.55);
    --leaf: #8ee05a;
    --rule: rgba(230, 210, 190, 0.55);
  }
  * { margin: 0; padding: 0; box-sizing: border-box; }
  html, body { width: 780px; height: 1200px; overflow: hidden; }
  body {
    background: var(--canvas);
    font-family: "Roboto Condensed", "Arial Narrow", sans-serif;
    position: relative;
  }
  .screen {
    position: absolute;
    left: 59px; top: 12px;
    width: 662px; height: 1176px;
    overflow: hidden;
    background: var(--plum);
  }
  .hero-photo {
    position: absolute; inset: 0;
    background: linear-gradient(160deg, var(--plum-deep) 0%, var(--plum) 55%, #76606f 100%);
  }
  .light-band { position: absolute; inset: 0; }
  .brand {
    position: absolute; left: 0; right: 0; top: 138px;
    display: flex; align-items: center; justify-content: center; gap: 16px;
  }
  .brand-dot {
    width: 22px; height: 22px; border-radius: 50%;
    background: var(--gold);
  }
  .brand-name {
    font-family: "Alegreya", Georgia, serif;
    font-weight: 500;
    font-size: 58px;
    color: var(--gold);
    line-height: 1;
  }
  .brand-rule {
    position: absolute; left: 86px; width: 488px; top: 251px;
    height: 1px; background: var(--rule);
  }
  .tagline {
    position: absolute; left: 0; right: 0; top: 268px;
    text-align: center;
    color: var(--ivory);
    font-weight: 300; font-size: 26px;
  }
  .steps-connector { position: absolute; left: 337px; top: 525px; }
  .step {
    position: absolute;
    display: flex; align-items: center; gap: 14px;
    color: var(--ivory);
    font-weight: 300; font-size: 34px;
    transform: translateY(-50%);
  }
  .step svg { width: 42px; height: 42px; flex: none; }
  .step-snapshot { left: 188px; top: 502px; }
  .step-describe { left: 157px; top: 602px; }
  .step-diagnosed { left: 189px; top: 703px; }
  .shop-button {
    position: absolute; left: 206px; top: 840px;
    width: 257px; height: 50px;
    border: 1.5px solid var(--mist); border-radius: 4px;
    display: flex; align-items: center; justify-content: center;
    color: var(--ivory); font-size: 22px; font-weight: 400;
  }
  .action {
    position: absolute; top: 935px;
    width: 284px; height: 68px; border-radius: 4px;
    display: flex; align-items: center; justify-content: center;
    color: var(--ivory); font-size: 26px; font-weight: 400;
  }
  .action-start { left: 30px; background: var(--copper); }
  .action-signin { left: 349px; background: var(--aubergine); }
  .partners {
    position: absolute; left: 0; right: 0; top: 1100px;
    height: 36px;
  }
  .partner {
    position: absolute; top: 0;
    transform: translateX(-50%);
    color: var(--mist);
    font-size: 28px; font-weight: 400;
    letter-spacing: 1px;
  }
  .partner-ostra { left: 96px; }
  .partner-toral { left: 234px; }
  .partner-norvexa { left: 402px; }
  .partner-lumavel { left: 569px; }
</style>
</head>
<body>
  <main class="screen">
    <div class="hero-photo" role="img" aria-label="Photograph of a woman with curly hair touching her bare shoulder, tinted in plum"></div>
    <svg class="light-band" viewBox="0 0 662 1176" preserveAspectRatio="none" aria-hidden="true">
      <polygon points="320,0 662,0 662,800" fill="var(--plum-light)" opacity="0.55"/>
    </svg>

    <header class="brand">
      <span class="brand-dot"></span>
      <span class="brand-name">Vessa Kliniq</span>
    </header>
    <div class="brand-rule"></div>
    <p class="tagline">Real Doctor Dermatology Consultation</p>

    <svg class="steps-connector" width="4" height="160" viewBox="0 0 4 160" aria-hidden="true">
      <line x1="2" y1="0" x2="2" y2="50" stroke="var(--mist)" stroke-width="2" stroke-dasharray="2 6"/>
      <line x1="2" y1="105" x2="2" y2="150" stroke="var(--mist)" stroke-width="2" stroke-dasharray="2 6"/>
    </svg>

    <ol>
      <li class="step step-snapshot">
        <svg viewBox="0 0 42 42" aria-hidden="true"><path d="M36 15 A17 17 0 1 1 28 6" fill="none" stroke="var(--ivory)" stroke-width="3" stroke-linecap="round"/><path d="M12 20 l8 8 L38 8" fill="none" stroke="var(--ivory)" stroke-width="3" stroke-linecap="round" stroke-linejoin="round"/></svg>
        <span>Take a Snapshot</span>
      </li>
      <li class="step step-describe">
        <svg viewBox="0 0 42 42" aria-hidden="true"><path d="M36 15 A17 17 0 1 1 28 6" fill="none" stroke="var(--ivory)" stroke-width="3" stroke-linecap="round"/><path d="M12 20 l8 8 L38 8" fill="none" stroke="var(--ivory)" stroke-width="3" stroke-linecap="round" stroke-linejoin="round"/></svg>
        <span>Describe and Send it</span>
      </li>
      <li class="step step-diagnosed">
        <svg viewBox="0 0 42 42" aria-hidden="true"><path d="M36 15 A17 17 0 1 1 28 6" fill="none" stroke="var(--leaf)" stroke-width="3" stroke-linecap="round"/><path d="M12 20 l8 8 L38 8" fill="none" stroke="var(--leaf)" stroke-width="3" stroke-linecap="round" stroke-linejoin="round"/></svg>
        <span>Get Diagnosed</span>
      </li>
    </ol>

    <a class="shop-button">Medical Cosmetics</a>
    <a class="action action-start">Start</a>
    <a class="action action-signin">Sign In</a>

    <nav class="partners" aria-label="Our partners">
      <span class="partner partner-ostra">Ostra</span>
      <span class="partner partner-toral">Toral</span>
      <span class="partner partner-norvexa">Norvexa</span>
      <span class="partner partner-lumavel">Lumavel</span>
    </nav>
  </main>
</body>
</html>
```